A new customer-driven VC fund for Enterprise IT Startups

I am bringing together a global group of customers (CIOs, CTOs, CISOs of Beacon 3000 companies) to help me identify and diligence best-of-breed Enterprise IT startups so I can invest in them via my new venture capital fund, Larkfen Ventures. In many ways, this is a new model for a VC fund and my goal is to revolutionize Venture Capital so that we hit the bull's eye in investing way more often in what is otherwise a guessing game for most VCs. So in the website, I'd like to capture the essences of global reach, best-of-breed, breakthrough innovation. I also want it to convey the ability of Larkfen Ventures to create category winners (i.e., if you want to be a market leader as a startup, you must take an investment from Larkfen Ventures).
My current website is www.larkfen-ventures.example - please use the content from the website within your design but please DO NOT use the design elements from the current website. INSTEAD, I'm looking for new and creative ideas on how I can leverage the existing content in a more appealing design -- any designs that look remotely similar to the existing website will be immediately declined.
I also want to ensure that the web design is mobile friendly.
Target Market(s)
Startup founders, potential investors, and other VCs
Industry/Entity Type
Venture Capital
Coding
Coded - Design and coding required
Number of Pages Required
1 page
Look and feel
Each slider illustrates characteristics of the customer's brand and the style your logo design should communicate.

```html
<!DOCTYPE html>
<html lang="en">
<head>
<meta charset="utf-8">
<title>Larkfen Ventures</title>
<link href="https://fonts.googleapis.com/css2?family=Saira+Semi+Condensed:wght@500;600;700&family=Open+Sans:wght@400;600;700&display=swap" rel="stylesheet">
<style>
:root{
  --teal:#3a8db3;
  --teal-dark:#1f6483;
  --navy:#1b2a38;
  --cyan:#84f1f8;
  --cyan-pale:#e4fbfd;
  --grey-bg:#f1f2f3;
  --text:#2a2f35;
  --muted:#4a5660;
  --white:#ffffff;
}
*{box-sizing:border-box;margin:0;padding:0}
html,body{width:1200px;height:4980px;overflow:hidden}
body{position:relative;background:var(--white);font-family:"Open Sans",sans-serif;color:var(--text)}
.abs{position:absolute}
.head{font-family:"Saira Semi Condensed",sans-serif}
.brand{display:flex;align-items:center;gap:10px;font-family:"Saira Semi Condensed",sans-serif;font-weight:700;color:var(--teal);white-space:nowrap}
.brand .dot{width:30px;height:30px;border-radius:50%;background:var(--teal)}
/* nav */
.nav{left:0;top:0;width:1200px;height:92px;background:var(--white)}
.nav .brand{position:absolute;left:175px;top:26px;font-size:28px}
.nav ul{position:absolute;right:170px;top:38px;display:flex;gap:26px;list-style:none;font-size:14px;color:var(--navy)}
/* hero */
.hero-bg{left:0;top:92px;width:1200px;height:600px;background:var(--grey-bg)}
.hero-photo{left:686px;top:92px;width:514px;height:700px;background:linear-gradient(160deg,#d9dcdf,#b9b3aa 45%,#8a8078 70%,#e8e8e8)}
.hero-title{left:172px;top:165px;font-weight:700;font-size:54px;color:var(--teal);line-height:1;white-space:nowrap}
.hero-sub1{left:172px;top:232px;font-weight:700;font-size:40px;line-height:1.1;color:var(--navy);white-space:nowrap}
.hero-sub2{left:172px;top:284px;font-weight:600;font-size:38px;line-height:1.1;color:var(--navy);white-space:nowrap}
.hero-text{left:172px;top:350px;width:520px;font-size:16px;line-height:28px;color:var(--navy)}
.btn{left:172px;top:429px;width:146px;height:50px;border-radius:25px;background:var(--teal);color:#fff;font-size:16px;display:flex;align-items:center;justify-content:center}
.dots{left:172px;top:518px;display:flex;gap:5px}
.dots i{width:12px;height:12px;border-radius:50%;background:#bbb}
.dots i:first-child{background:#111}
/* section headings */
.sec-head{left:0;width:1200px;text-align:center}
.sec-head .mark{font-family:"Saira Semi Condensed",sans-serif;font-weight:700;font-size:28px;color:var(--teal);line-height:1.1}
.sec-head h2{font-family:"Saira Semi Condensed",sans-serif;font-weight:700;font-size:32px;color:var(--navy);line-height:1.2;white-space:nowrap}
.sec-head.light h2{color:#fff}
.sec-head.light .mark{color:var(--cyan)}
.lead{left:200px;width:800px;text-align:center;font-size:15px;line-height:25px;color:var(--navy)}
.lead.light{color:#fff}
/* who cards */
.card{width:261px;height:363px;border-radius:24px;background:#fff;box-shadow:0 6px 18px rgba(0,0,0,.15);overflow:hidden;text-align:center}
.card .photo{height:164px;background:linear-gradient(135deg,#9fb6c7,#d7d2cb 50%,#6f7f8d)}
.card h3{font-family:"Saira Semi Condensed",sans-serif;font-weight:600;font-size:16px;margin:22px 0 10px;color:var(--navy);white-space:nowrap}
.card p{font-size:10.5px;line-height:18px;padding:0 18px;color:var(--muted)}
/* focus */
.focus-item{width:200px}
.focus-item h4{font-family:"Saira Semi Condensed",sans-serif;font-weight:700;font-size:16px;line-height:19px;color:var(--navy);white-space:nowrap}
.focus-item p{font-size:11.5px;line-height:16px;color:var(--muted);width:180px}
.focus-item.left{text-align:right}
.focus-item.left p{margin-left:auto}
.icon-dot{width:58px;height:58px;border-radius:50%;background:#fff;box-shadow:0 3px 10px rgba(0,0,0,.15);display:flex;align-items:center;justify-content:center}
.icon-dot span{width:44px;height:44px;border-radius:50%;background:var(--teal);display:flex;align-items:center;justify-content:center}
/* numbers */
.pill{width:240px;height:136px;border-radius:68px;background:var(--cyan);border:3px solid #fff;display:flex;align-items:center;padding:6px;overflow:hidden}
.pill b{width:110px;height:110px;border-radius:50%;background:var(--teal);color:#fff;font-family:"Saira Semi Condensed",sans-serif;font-size:26px;display:flex;align-items:center;justify-content:center;text-align:center;line-height:1.05;flex-shrink:0}
.pill span{font-size:11.5px;line-height:17px;color:var(--navy);padding:0 14px 0 12px}
/* themes */
.theme-photo{left:174px;top:3052px;width:448px;height:426px;border-radius:200px 60px 200px 60px;background:linear-gradient(140deg,#e9e4dc,#a79d92 50%,#3f4a5a)}
.theme{left:676px;display:flex;align-items:center;gap:30px}
.theme .ic{width:77px;height:77px;border-radius:50%;background:var(--teal-dark);display:flex;align-items:center;justify-content:center;flex-shrink:0}
.theme h4{font-family:"Saira Semi Condensed",sans-serif;font-weight:700;font-size:21px;line-height:28px;color:var(--navy);white-space:nowrap}
/* team */
.member{width:200px;text-align:center;color:#fff}
.member .av{width:124px;height:124px;margin:0 auto;border-radius:50%;border:6px solid var(--cyan);background:radial-gradient(circle at 50% 40%,#c8b6a6,#5b6470)}
.member h5{font-family:"Saira Semi Condensed",sans-serif;font-weight:600;font-size:19px;margin-top:12px;white-space:nowrap}
.member p{font-family:"Saira Semi Condensed",sans-serif;font-size:12px;line-height:17px}
/* engine */
.ecard{width:261px;height:323px;border-radius:60px 24px 60px 24px;background:#fff;box-shadow:0 6px 18px rgba(0,0,0,.18);overflow:hidden;text-align:center}
.ecard .corner{position:absolute;right:0;top:0;width:134px;height:120px;border-radius:0 0 0 70px;background:var(--teal);display:flex;align-items:center;justify-content:center}
.ecard h3{font-family:"Saira Semi Condensed",sans-serif;font-weight:600;font-size:17px;margin:152px 0 12px;color:var(--navy);white-space:nowrap}
.ecard p{font-size:10.5px;line-height:18px;padding:0 22px;color:var(--muted)}
.ecard.featured{background:var(--teal)}
.ecard.featured .corner{background:var(--cyan)}
.ecard.featured h3,.ecard.featured p{color:#fff}
/* footer */
.footer{left:0;top:4888px;width:1200px;height:92px;background:var(--teal-dark)}
.footer .brand{position:absolute;left:175px;top:30px;font-size:26px;color:#fff}
.footer .brand .dot{background:#fff}
.footer small{position:absolute;right:172px;top:38px;font-size:13px;color:#fff}
</style>
</head>
<body>

<header class="abs nav">
  <div class="brand"><span class="dot"></span>Larkfen Ventures</div>
  <ul><li>ABOUT</li><li>NETWORK</li><li>TEAM &amp; ADVISORS</li><li>GTM ENGINE</li></ul>
</header>

<section>
  <div class="abs hero-bg"></div>
  <div class="abs hero-photo" role="img" aria-label="Smiling man working on a laptop and taking notes"></div>
  <div class="abs hero-title head">WE INVEST IN</div>
  <div class="abs hero-sub1 head">ENTERPRISE IT STARTUPS</div>
  <div class="abs hero-sub2 head">at the Product-Market-Fit Stage</div>
  <p class="abs hero-text">We are singularly focused on helping our portfolio companies gain a massive competitive advantage</p>
  <div class="abs btn">READ MORE</div>
  <div class="abs dots"><i></i><i></i><i></i></div>
</section>

<section>
  <div class="abs sec-head" style="top:862px"><div class="mark">Larkfen Ventures</div><h2>WHO WE ARE</h2></div>
  <p class="abs lead" style="top:962px">We only invest in post-product, post-revenue Enterprise IT startups. Usually, this means you're at Seed Extension to Series A stage.</p>
  <div class="abs card" style="left:172px;top:1049px">
    <div class="photo" role="img" aria-label="Business people shaking hands in an office"></div>
    <h3>CUSTOMERS</h3>
    <p>Hundreds of the earliest-adopting CIOs, CTOs, and CISOs from Beacon 10 to Summit 2000 to Cloud-First companies are a part of our exclusive network. An investment from Larkfen Ventures will give you immediate and exclusive access to hundreds of buyers around the world.</p>
  </div>
  <div class="abs card" style="left:469px;top:1049px">
    <div class="photo" role="img" aria-label="Team meeting around a table"></div>
    <h3>OUR INVESTMENT PHILOSOPHY</h3>
    <p>We only invest in startups that have broad &amp; immediate applicability across a global CIO base and are solving critical problems. To give our portfolio companies a truly unfair competitive advantage, we do not invest in competitive startups.</p>
  </div>
  <div class="abs card" style="left:767px;top:1049px">
    <div class="photo" role="img" aria-label="Colleagues reviewing documents together"></div>
    <h3>CUSTOMER-LED INVESTMENTS</h3>
    <p>A global roster of CIOs leads our investment decision-making process. We also share candid, unfiltered feedback from dozens of customers via a Larkfen Memo with every single startup who presents to us - even if we don't end up investing.</p>
  </div>
</section>

<svg class="abs" style="left:0;top:1460px" width="1200" height="1380" viewBox="0 0 1200 1380">
  <polygon points="0,90 310,12 770,165 1200,55 1200,820 770,900 0,780" fill="var(--cyan-pale)"/>
  <polyline points="0,92 310,14 770,168 1200,58" fill="none" stroke="#2e7fa3" stroke-width="6"/>
  <polygon points="0,820 760,900 1200,765 1200,1367 0,1367" fill="var(--teal-dark)"/>
  <polyline points="760,898 1200,762" fill="none" stroke="var(--cyan)" stroke-width="10"/>
</svg>

<section>
  <div class="abs sec-head" style="top:1662px"><div class="mark">Larkfen Ventures</div><h2>INVESTMENT FOCUS AREAS</h2></div>
  <svg class="abs" style="left:380px;top:1718px" width="440" height="440" viewBox="0 0 440 440">
    <path d="M20,220 A200,200 0 1,0 420,220" fill="none" stroke="#b8c6cc" stroke-width="2"/>
    <circle cx="220" cy="220" r="150" fill="#fff"/>
    <defs><linearGradient id="orb" x1="0" y1="0" x2="0" y2="1"><stop offset="0" stop-color="#8ff3f8"/><stop offset="1" stop-color="#3a8db3"/></linearGradient></defs>
    <circle cx="220" cy="220" r="140" fill="url(#orb)"/>
    <text x="220" y="232" text-anchor="middle" font-family="Saira Semi Condensed, sans-serif" font-weight="700" font-size="40" fill="#fff">Larkfen</text>
  </svg>
  <div class="abs focus-item left" style="left:158px;top:1840px"><h4>SECURITY</h4><p>Duis aute irure dolor in reprehen derit in voluptate</p></div>
  <div class="abs icon-dot" style="left:372px;top:1840px"><span><svg width="22" height="22" viewBox="0 0 24 24"><path d="M12 2l8 3v6c0 5-3.5 9-8 11-4.5-2-8-6-8-11V5z" fill="none" stroke="#fff" stroke-width="2"/></svg></span></div>
  <div class="abs focus-item left" style="left:150px;top:1938px"><h4>AI &amp; ML</h4><p>Duis aute irure dolor in reprehen derit in voluptate</p></div>
  <div class="abs icon-dot" style="left:364px;top:1936px"><span><svg width="22" height="22" viewBox="0 0 24 24"><rect x="6" y="6" width="12" height="12" rx="2" fill="none" stroke="#fff" stroke-width="2"/><path d="M9 2v4M15 2v4M9 18v4M15 18v4M2 9h4M2 15h4M18 9h4M18 15h4" stroke="#fff" stroke-width="2"/></svg></span></div>
  <div class="abs focus-item left" style="left:188px;top:2036px"><h4>NETWORKING &amp;<br>ARCHITECTURE</h4><p>Duis aute irure dolor in reprehen derit in voluptate</p></div>
  <div class="abs icon-dot" style="left:402px;top:2036px"><span><svg width="22" height="22" viewBox="0 0 24 24"><circle cx="12" cy="12" r="9" fill="none" stroke="#fff" stroke-width="2"/><path d="M3 12h18M12 3c3 3 3 15 0 18M12 3c-3 3-3 15 0 18" fill="none" stroke="#fff" stroke-width="1.6"/></svg></span></div>
  <div class="abs icon-dot" style="left:765px;top:1840px"><span><svg width="24" height="22" viewBox="0 0 24 24"><path d="M7 18h11a4 4 0 000-8 6 6 0 00-11-1 4.5 4.5 0 000 9z" fill="none" stroke="#fff" stroke-width="2"/></svg></span></div>
  <div class="abs focus-item" style="left:840px;top:1840px"><h4>CLOUD &amp;<br>INFRASTRUCTURE</h4><p>Duis aute irure dolor in reprehen derit in voluptate</p></div>
  <div class="abs icon-dot" style="left:772px;top:1938px"><span><svg width="24" height="22" viewBox="0 0 24 24"><path d="M12 12c-2-3-7-3-7 0s5 3 7 0 7-3 7 0-5 3-7 0" fill="none" stroke="#fff" stroke-width="2"/></svg></span></div>
  <div class="abs focus-item" style="left:848px;top:1938px"><h4>DEVOPS</h4><p>Duis aute irure dolor in reprehen derit in voluptate</p></div>
  <div class="abs icon-dot" style="left:738px;top:2036px"><span><svg width="24" height="22" viewBox="0 0 24 24"><path d="M7 18h11a4 4 0 000-8 6 6 0 00-11-1 4.5 4.5 0 000 9z" fill="none" stroke="#fff" stroke-width="2"/></svg></span></div>
  <div class="abs focus-item" style="left:810px;top:2036px"><h4>SAAS</h4><p>Duis aute irure dolor in reprehen derit in voluptate</p></div>
</section>

<section>
  <div class="abs sec-head light" style="top:2384px"><div class="mark">Larkfen Ventures</div><h2>STRENGTH IN NUMBERS</h2></div>
  <p class="abs lead light" style="top:2480px;left:330px;width:540px">We collect and analyze monthly purchase intent data from a global network of IT decision-makers.</p>
  <div class="abs pill" style="left:97px;top:2589px"><b>500+</b><span>Early adopting, influential CIOs, CTOs, CISOs and IT decision-makers</span></div>
  <div class="abs pill" style="left:354px;top:2589px"><b>$<br>100B+</b><span>Annual enterprise technology purchasing budget across our network</span></div>
  <div class="abs pill" style="left:609px;top:2589px"><b>15</b><span>Countries represented in our current network</span></div>
  <div class="abs pill" style="left:862px;top:2589px"><b>550+</b><span>Purchase intent data points collected monthly</span></div>
</section>

<section>
  <div class="abs sec-head" style="top:2900px"><div class="mark">Larkfen Ventures</div><h2>UNIFYING INVESTMENT THEMES</h2></div>
  <div class="abs theme-photo" role="img" aria-label="Bearded executive in a suit looking at a tablet"></div>
  <div class="abs theme" style="top:3112px"><div class="ic"><svg width="40" height="40" viewBox="0 0 24 24"><circle cx="12" cy="12" r="9" fill="none" stroke="#fff" stroke-width="1.6"/><path d="M3 12h18M12 3c3 3 3 15 0 18M12 3c-3 3-3 15 0 18" fill="none" stroke="#fff" stroke-width="1.4"/></svg></div><h4>Next-Gen Enterprise<br>IT Solutions</h4></div>
  <div class="abs theme" style="top:3232px"><div class="ic"><svg width="40" height="40" viewBox="0 0 24 24"><path d="M12 2.5l2.9 6 6.6.8-4.9 4.6 1.3 6.6L12 17.3l-5.9 3.2 1.3-6.6L2.5 9.3l6.6-.8z" fill="none" stroke="#fff" stroke-width="1.6"/></svg></div><h4>Attacking Large Markets<br>With Universal Application</h4></div>
  <div class="abs theme" style="top:3352px"><div class="ic"><svg width="40" height="40" viewBox="0 0 24 24"><path d="M12 3l9 5-9 5-9-5z" fill="none" stroke="#fff" stroke-width="1.6"/><path d="M3 12l9 5 9-5M3 16l9 5 9-5" fill="none" stroke="#fff" stroke-width="1.6"/></svg></div><h4>Products And Platforms<br>That Take A Holistic<br>Approach</h4></div>
</section>

<svg class="abs" style="left:0;top:3525px" width="1200" height="760" viewBox="0 0 1200 760">
  <polygon points="0,78 310,0 770,150 1200,40 1200,760 0,760" fill="var(--teal-dark)"/>
  <polyline points="0,80 310,3" fill="none" stroke="var(--cyan)" stroke-width="10"/>
</svg>

<section>
  <div class="abs sec-head light" style="top:3712px"><div class="mark">Larkfen Ventures</div><h2>TEAM, INVESTORS &amp; ADVISORS</h2></div>
  <p class="abs lead light" style="top:3805px;left:170px;width:860px">We have built a world-class roster of executive advisors and mentors with exceptional go-to-market pedigrees to help our portfolio companies in their go-to-market journeys.</p>
  <div class="abs member" style="left:62px;top:3929px"><div class="av" role="img" aria-label="Portrait of Rafiq D. Hollan"></div><h5>Rafiq D. Hollan</h5><p>Founder &amp; Managing Director</p></div>
  <div class="abs member" style="left:242px;top:3899px"><div class="av" role="img" aria-label="Portrait of Martin Lisle"></div><h5>Martin Lisle</h5><p>Founder &amp; Ex CEO, Stellhaven Data</p></div>
  <div class="abs member" style="left:412px;top:3966px"><div class="av" role="img" aria-label="Portrait of Anand Sethi"></div><h5>Anand Sethi</h5><p>Co-founder, Nodarix (IPO),<br>Querywell</p></div>
  <div class="abs member" style="left:586px;top:3933px"><div class="av" role="img" aria-label="Portrait of Tobin Sharif"></div><h5>Tobin Sharif</h5><p>Co-founder, Quarrylake<br>($2B+ valuation)</p></div>
  <div class="abs member" style="left:773px;top:3895px"><div class="av" role="img" aria-label="Portrait of Theo Kranz"></div><h5>Theo Kranz</h5><p>President, Corvane Chips</p></div>
  <div class="abs member" style="left:945px;top:3957px"><div class="av" role="img" aria-label="Portrait of Arjun Seth"></div><h5>Arjun Seth</h5><p>Executive Director, Brambleworks Design</p></div>
</section>

<section>
  <div class="abs sec-head" style="top:4346px"><div class="mark">Larkfen Ventures</div><h2>A GLOBAL GTM ENGINE</h2></div>
  <div class="abs ecard" style="left:172px;top:4478px">
    <div class="corner"><svg width="50" height="50" viewBox="0 0 24 24"><rect x="7" y="3" width="13" height="16" rx="1" fill="none" stroke="#fff" stroke-width="1.6"/><path d="M10 8h7M10 11h7M10 14h4" stroke="#fff" stroke-width="1.4"/><circle cx="6" cy="16" r="4" fill="#fff"/></svg></div>
    <h3>GTM COACHES</h3>
    <p>We will partner with you to navigate the complex enterprise sales process by leveraging our executive network to provide product feedback, sales strategy, and market insights.</p>
  </div>
  <div class="abs ecard featured" style="left:469px;top:4478px">
    <div class="corner"><svg width="56" height="40" viewBox="0 0 28 20"><path d="M2 6l6-3 6 4 6-4 6 3v6l-8 6-4-3-4 3-8-6z" fill="none" stroke="#1f6483" stroke-width="1.6"/></svg></div>
    <h3>STRATEGIC PARTNERS</h3>
    <p>Strategic partnerships can propel a startup to the next level. Leverage our extensive network of IT Executives, Channel Partners, and OEMs to accelerate your path to becoming a category leader.</p>
  </div>
  <div class="abs ecard" style="left:767px;top:4478px">
    <div class="corner"><svg width="50" height="50" viewBox="0 0 24 24"><circle cx="12" cy="12" r="9" fill="none" stroke="#fff" stroke-width="1.8"/><path d="M7 8c2 0 3 2 2 4s1 3 2 5M15 5c-1 2 1 3 3 3M14 14c1 1 3 1 4-1" fill="none" stroke="#fff" stroke-width="1.4"/></svg></div>
    <h3>GLOBAL AMBASSADORS</h3>
    <p>Expanding globally is no simple exercise. Our network of Global IT Execs will provide on-the-ground intelligence, referrals, and influence as you conquer new geographies.</p>
  </div>
</section>

<footer class="abs footer">
  <div class="brand"><span class="dot"></span>Larkfen Ventures</div>
  <small>Copyrights @ 2021 Larkfen Ventures. All Rights Reserved.</small>
</footer>

</body>
</html>
```